Velmira - New coded website

Current website is around 5 years old and corrupted in some ways...
I would like to refresh the design and to create a new coded website based on the current content .
Please refer to :
www.velmira.com.au

Coding

Coded - Design and coding required

```html
<!DOCTYPE html>
<html lang="en">
<head>
<meta charset="utf-8">
<title>Velmira – Odours Controlled Naturally</title>
<link href="https://fonts.googleapis.com/css2?family=Lato:wght@300;400;700;900&display=swap" rel="stylesheet">
<style>
:root{
  --green:#2e8b57;
  --green-dark:#1f6b45;
  --leaf:#6ab04c;
  --band:#4f8a35;
  --band-dark:#3f7a2a;
  --ink:#111;
  --muted:#555;
  --white:#fff;
  --footer:#000;
  --line:#c9c9c9;
}
*{margin:0;padding:0;box-sizing:border-box}
html,body{width:1200px;height:3692px;overflow:hidden}
body{font-family:'Lato',sans-serif;color:var(--ink);background:var(--white);position:relative}
.abs{position:absolute}
a{color:inherit;text-decoration:none}

/* hero */
.hero{left:0;top:0;width:1200px;height:643px;background:linear-gradient(180deg,#7a8a8c 0%,#5d6a4a 30%,#2f4630 55%,#28402f 75%,#1f2d28 100%)}
.logo{display:flex;align-items:center;gap:10px;font-weight:400;font-size:32px}
.logo-mark{width:58px;height:58px;border-radius:50%;background:var(--leaf)}
.logo small{display:block;font-size:11px;font-style:italic;font-weight:300;margin-top:-2px}
.nav{left:355px;top:34px;display:flex;gap:16px;color:var(--white);font-size:14.5px;font-weight:700;white-space:nowrap}
.hero-title{left:0;width:1200px;top:168px;text-align:center;color:var(--white);font-size:53px;font-weight:700;line-height:65px}
.btn{display:flex;align-items:center;border:2px solid var(--green);font-weight:700;font-size:16px;height:44px;white-space:nowrap}
.btn span{padding:0 12px;flex:1 1 auto}
.btn i{display:flex;align-items:center;justify-content:center;width:40px;height:100%;background:var(--green);flex:0 0 40px}
.btn-dark{background:rgba(0,0,0,.25);color:var(--white)}
.follow{left:63px;top:583px;color:var(--white);font-size:15px;font-weight:700;display:flex;align-items:center;gap:12px}
.follow hr{width:84px;border:0;border-top:1px solid #ddd}
.social{width:32px;height:32px;border-radius:50%;background:var(--white)}
.hero-contact{color:var(--white);font-size:15px;font-weight:700;display:flex;gap:8px;line-height:25px;white-space:nowrap}

/* about */
h2{font-size:35px;font-weight:700;line-height:36px}
.about-text{left:112px;top:788px;width:490px;font-size:12.6px;line-height:26px;color:var(--muted)}
.brand-disc{left:687px;top:697px;width:320px;height:320px;border-radius:50%;background:var(--green);display:flex;align-items:center;justify-content:center;color:var(--white);font-size:44px;font-weight:700}

/* cards */
.card{top:1102px;width:297px;height:298px;border:2px solid var(--green);box-shadow:0 4px 8px rgba(0,0,0,.12)}
.card-icon{position:absolute;left:78px;top:24px;width:140px;height:140px;border-radius:50%;background:var(--white);box-shadow:0 2px 10px rgba(0,0,0,.18);display:flex;align-items:center;justify-content:center}
.card-label{position:absolute;top:200px;width:100%;text-align:center;font-size:23px;font-weight:700}
.card-arrow{position:absolute;right:0;bottom:0;width:38px;height:40px;background:var(--green);display:flex;align-items:center;justify-content:center}

/* bands */
.band{left:0;width:1200px;background:linear-gradient(180deg,var(--band) 0%,#5f9a3f 60%,var(--band-dark) 100%)}
.band-title{left:0;width:1200px;text-align:center;color:var(--white);font-size:34px;font-weight:700}
.video{left:286px;top:1580px;width:628px;height:268px;background:linear-gradient(180deg,#f6fbf0 0%,#e8f4dc 60%,#3aa77a 100%);display:flex;align-items:center;justify-content:center}

.photo-hills{left:112px;top:1980px;width:455px;height:250px;background:linear-gradient(180deg,#d99a3c 0%,#8b9a52 40%,#6a9a3a 70%,#88b544 100%)}
.best-list{left:598px;top:2040px;list-style:none;font-size:16px;color:var(--muted)}
.best-list li{display:flex;align-items:center;gap:9px;height:36px}

.quote-head{left:0;width:1200px;top:2408px;text-align:center;color:var(--white);font-size:23px;font-weight:700}
.quote-body{left:160px;top:2444px;width:880px;text-align:center;color:var(--white);font-size:12.5px;line-height:30px}
.quote-mark{color:rgba(255,255,255,.75);font-size:90px;font-weight:900;line-height:1}

.client{top:2818px;height:112px;display:flex;align-items:center;justify-content:center;gap:8px;font-size:19px;font-weight:700;color:#1b3a6b;white-space:nowrap}
.dot{width:26px;height:26px;border-radius:50%}

.map{left:0;top:3005px;width:1200px;height:370px;background:linear-gradient(135deg,#eef0f2 0%,#e4e8ea 100%)}
.form{left:112px;top:3048px;width:460px;height:394px;background:var(--white);padding:0 26px;box-shadow:0 0 12px rgba(0,0,0,.06);z-index:2}
.field{position:absolute;left:26px;width:410px;font-size:12.5px;color:var(--muted);border-bottom:1px solid var(--line);padding-bottom:8px}

.footer{left:0;top:3375px;width:1200px;height:317px;background:var(--footer);color:var(--white);z-index:1}
.f-col h3{font-size:20px;font-weight:700;margin-bottom:18px;white-space:nowrap}
.f-col p{font-size:12.5px;line-height:36px;white-space:nowrap}
.f-field{width:265px;font-size:12.5px;border-bottom:1px solid #bbb;padding-bottom:7px;margin-bottom:16px}
</style>
</head>
<body>

<!-- HERO -->
<div class="abs hero" role="img" aria-label="Mountain lake reflecting a forested alpine range at sunset"></div>
<div class="abs logo" style="left:86px;top:10px;color:var(--white)"><div class="logo-mark"></div><div>Velmira<small>odours controlled naturally</small></div></div>
<nav class="abs nav"><a>Odour Control Products</a><a>How Biofiltration Works</a><a>Odour Control by Industry</a><a>Past Projects</a><a>About Us</a><a>Contact</a></nav>
<h1 class="abs hero-title">Odours Controlled<br>Naturally</h1>
<a class="abs btn btn-dark" style="left:516px;top:307px;width:188px"><span>Request a quote</span><i><svg width="26" height="10" viewBox="0 0 26 10"><path d="M0 5h24M19 1l5 4-5 4" stroke="#fff" stroke-width="1.6" fill="none"/></svg></i></a>
<div class="abs follow">Follow Us <hr><div class="social"></div><span style="font-size:12px;font-weight:400">Netlink</span></div>
<div class="abs hero-contact" style="left:722px;top:582px"><svg width="18" height="18" viewBox="0 0 24 24"><path fill="#fff" d="M6.6 10.8a15 15 0 006.6 6.6l2.2-2.2c.3-.3.7-.4 1-.2 1.1.4 2.3.6 3.6.6.6 0 1 .4 1 1V20c0 .6-.4 1-1 1A17 17 0 013 4c0-.6.4-1 1-1h3.5c.6 0 1 .4 1 1 0 1.3.2 2.5.6 3.6.1.3 0 .7-.2 1z"/></svg>+61 (08) 5550 1420</div>
<div class="abs hero-contact" style="left:897px;top:580px"><svg width="14" height="20" viewBox="0 0 14 20"><path fill="#fff" d="M7 0a7 7 0 00-7 7c0 5 7 13 7 13s7-8 7-13a7 7 0 00-7-7zm0 9.5A2.5 2.5 0 117 4.5a2.5 2.5 0 010 5z"/></svg><div>14 Marrow Lane, Kelbrook<br>WA 6071, Australia</div></div>

<!-- ABOUT -->
<h2 class="abs" style="left:112px;top:701px">Odour Control Solutions |<br>About Velmira</h2>
<p class="abs about-text">Velmira uses sustainable biotechnology to resolve odour and corrosion problems in a highly efficient, environmentally friendly and cost-effective manner. Our, products, the VelVent series of biofilters have been specifically engineered to overcome issues traditionally associated with biofiltration, such as bed compaction and uneven moisture levels, and our patented design achieves a removal rate of up to 99.9% per stage of treatment.</p>
<a class="abs btn" style="left:113px;top:964px;width:188px;color:var(--ink)"><span>Request a quote</span><i><svg width="26" height="10" viewBox="0 0 26 10"><path d="M0 5h24M19 1l5 4-5 4" stroke="#fff" stroke-width="1.6" fill="none"/></svg></i></a>
<div class="abs brand-disc">Velmira</div>

<!-- CARDS -->
<div class="abs card" style="left:112px">
  <div class="card-icon"><svg width="64" height="64" viewBox="0 0 64 64"><path d="M32 6 58 18v28L32 58 6 46V18z" fill="var(--green)"/><path d="M6 18l26 12 26-12M32 30v28" stroke="#fff" stroke-width="2.5" fill="none"/></svg></div>
  <div class="card-label">Products</div>
  <div class="card-arrow"><svg width="26" height="10" viewBox="0 0 26 10"><path d="M0 5h24M19 1l5 4-5 4" stroke="#fff" stroke-width="1.6" fill="none"/></svg></div>
</div>
<div class="abs card" style="left:450px">
  <div class="card-icon"><svg width="70" height="70" viewBox="0 0 70 70"><circle cx="35" cy="16" r="9" fill="var(--green)"/><circle cx="25" cy="32" r="9" fill="var(--green)"/><circle cx="45" cy="32" r="9" fill="var(--green)"/><path d="M6 50c8-6 16-6 24-2h14c3 0 3 5 0 5H30l14 0c6 0 12-6 18-8v8c-8 6-20 12-34 8l-22-4z" fill="var(--green)"/></svg></div>
  <div class="card-label">Features</div>
  <div class="card-arrow"><svg width="26" height="10" viewBox="0 0 26 10"><path d="M0 5h24M19 1l5 4-5 4" stroke="#fff" stroke-width="1.6" fill="none"/></svg></div>
</div>
<div class="abs card" style="left:789px">
  <div class="card-icon"><svg width="64" height="64" viewBox="0 0 64 64"><circle cx="30" cy="28" r="14" fill="none" stroke="var(--green)" stroke-width="4"/><rect x="24" y="42" width="12" height="10" fill="var(--green)"/><circle cx="44" cy="18" r="7" fill="var(--leaf)"/><path d="M30 4v6M10 28H4M56 28h-6M14 12l4 4M46 44l4 4" stroke="var(--green)" stroke-width="3"/></svg></div>
  <div class="card-label">Past Projects</div>
  <div class="card-arrow"><svg width="26" height="10" viewBox="0 0 26 10"><path d="M0 5h24M19 1l5 4-5 4" stroke="#fff" stroke-width="1.6" fill="none"/></svg></div>
</div>

<!-- VIDEO -->
<div class="abs band" style="top:1474px;height:447px"></div>
<h2 class="abs band-title" style="top:1512px">Watch Our Video</h2>
<div class="abs video" role="img" aria-label="Animated explainer still showing trees and biofilter tanks with a play button">
  <svg width="56" height="56" viewBox="0 0 56 56"><circle cx="28" cy="28" r="27" fill="#3aa77a"/><path d="M22 16l18 12-18 12z" fill="#fff"/></svg>
</div>

<!-- WHY US -->
<div class="abs photo-hills" role="img" aria-label="Misty green hills at sunrise"></div>
<h2 class="abs" style="left:598px;top:1988px;font-size:33px">What makes us the best?</h2>
<ul class="abs best-list">
  <li><svg width="28" height="28" viewBox="0 0 28 28"><circle cx="14" cy="14" r="14" fill="var(--green)"/><path d="M7 14l5 5 9-10" stroke="#fff" stroke-width="3" fill="none"/></svg>Biological &amp; Sustainable technology</li>
  <li><svg width="28" height="28" viewBox="0 0 28 28"><circle cx="14" cy="14" r="14" fill="var(--green)"/><path d="M7 14l5 5 9-10" stroke="#fff" stroke-width="3" fill="none"/></svg>Efficient maintenance cost</li>
  <li><svg width="28" height="28" viewBox="0 0 28 28"><circle cx="14" cy="14" r="14" fill="var(--green)"/><path d="M7 14l5 5 9-10" stroke="#fff" stroke-width="3" fill="none"/></svg>100% Australian Owned</li>
  <li><svg width="28" height="28" viewBox="0 0 28 28"><circle cx="14" cy="14" r="14" fill="var(--green)"/><path d="M7 14l5 5 9-10" stroke="#fff" stroke-width="3" fill="none"/></svg>Eco Friendly</li>
</ul>

<!-- TESTIMONIALS -->
<div class="abs band" style="top:2298px;height:409px"></div>
<h2 class="abs band-title" style="top:2339px">Testimonials</h2>
<div class="abs quote-mark" style="left:186px;top:2380px">&ldquo;</div>
<div class="abs quote-head">As soon as the system was started, the smell disappeared!</div>
<p class="abs quote-body">"Tomas and the Velmira team promised to stop the odour from our smelly neighbor and they delivered- in spades! As soon as the system was started, the smell disappeared. The system is well designed, very professionally installed and the beauty of it is, apart from a constantly running fan, it is bacteria doing the heavy lifting, so it is very environmentally friendly. We lived with the smell for 3 three years which could be extremely frustrating and unpleasant. Now, the problem is solved and we can have BBQs again. We are happy and our neighbours have noticed the odour is gone. Thank you!"</p>
<div class="abs quote-mark" style="left:940px;top:2565px">&rdquo;</div>
<div class="abs" style="left:0;width:1200px;top:2603px;text-align:center;color:var(--white);font-size:20px;font-weight:700">Rowan Pell</div>
<div class="abs" style="left:0;width:1200px;top:2636px;text-align:center;color:var(--white);font-size:12.5px">Nearby resident to Hollis Road Wastewater Pump Station</div>

<!-- CLIENTS -->
<h2 class="abs" style="left:0;width:1200px;top:2750px;text-align:center;font-size:33px">Our Happy Clients</h2>
<svg class="abs" style="left:58px;top:2872px" width="16" height="26" viewBox="0 0 16 26"><path d="M13 2 3 13l10 11" stroke="#111" stroke-width="3" fill="none"/></svg>
<svg class="abs" style="left:1130px;top:2872px" width="16" height="26" viewBox="0 0 16 26"><path d="M3 2l10 11L3 24" stroke="#111" stroke-width="3" fill="none"/></svg>
<div class="abs client" style="left:140px;width:180px"><div class="dot" style="background:#1b3a6b"></div>Corran Water</div>
<div class="abs client" style="left:320px;width:200px"><div class="dot" style="background:#e36b1c"></div>Eastvale Council</div>
<div class="abs client" style="left:520px;width:180px">Harbour City</div>
<div class="abs client" style="left:705px;width:175px;color:#444">Sandmere Shire</div>
<div class="abs client" style="left:880px;width:210px;color:#2a5aa8">Tidewell Utilities</div>

<!-- CONTACT -->
<div class="abs map" role="img" aria-label="Street map of the office location with a red marker"></div>
<form class="abs form">
  <h2 style="position:absolute;top:38px;font-size:33px">Get In Touch</h2>
  <div class="field" style="top:90px">Name</div>
  <div class="field" style="top:133px">Email</div>
  <div class="field" style="top:175px">Contact Number</div>
  <div class="field" style="top:216px;height:70px">Message</div>
  <div class="btn" style="position:absolute;left:24px;top:306px;width:136px"><span>Submit</span><i><svg width="22" height="10" viewBox="0 0 26 10"><path d="M0 5h24M19 1l5 4-5 4" stroke="#fff" stroke-width="1.6" fill="none"/></svg></i></div>
</form>

<!-- FOOTER -->
<footer class="abs footer">
  <div class="abs logo" style="left:112px;top:88px;color:var(--white)"><div class="logo-mark"></div><div>Velmira<small>odours controlled naturally</small></div></div>
  <div class="abs" style="left:118px;top:190px;display:flex;align-items:center;gap:8px;font-size:13px"><div style="width:24px;height:24px;background:var(--white)"></div>Netlink</div>
  <div class="abs" style="left:112px;top:232px;font-size:12.5px;white-space:nowrap">© 2023 Velmira. All rights reserved.</div>
  <div class="abs f-col" style="left:370px;top:96px"><h3>Quick Links</h3><div style="margin-top:-8px"><p>Odour Control Products</p><p>How Biofiltration Works</p><p>Odour Control by Industry</p><p>Past Projects</p><p>About Us</p></div></div>
  <div class="abs f-col" style="left:582px;top:96px"><h3>Contact Us</h3><div style="margin-top:-8px"><p>&#9990; +61 (08) 5550 1420</p><p>&#9679; 14 Marrow Lane, Kelbrook</p><p style="padding-left:14px">WA 6071, Australia</p></div></div>
  <div class="abs f-col" style="left:822px;top:96px"><h3>Sign Up For Our Newsletter</h3>
    <div class="f-field">Name</div><div class="f-field">Email</div>
    <div class="btn" style="width:136px;color:var(--white)"><span>Sign Up</span><i><svg width="22" height="10" viewBox="0 0 26 10"><path d="M0 5h24M19 1l5 4-5 4" stroke="#fff" stroke-width="1.6" fill="none"/></svg></i></div>
  </div>
</footer>
</body>
</html>
```